New Web Design Project

New Roofing Website homepage mockup

Complete design document here: https://files.plenovark.com/document/d/7kRtWmZpQ2vLxB9nHcYdF4sJgTuEaOiMbNwXzCyVqhr/edit?usp=sharing
Updates

PROJECT IS NOW CLOSED. ANY NEW SUBMISSIONS WILL BE AUTO REJECTED

Number of Pages Required

1 page

Font styles to use
Sans Serif

```html
<!DOCTYPE html>
<html lang="en">
<head>
<meta charset="utf-8">
<title>Steadfast Roofing – Homepage</title>
<link href="https://fonts.googleapis.com/css2?family=Open+Sans:ital,wght@0,400;0,600;0,700;1,400&display=swap" rel="stylesheet">
<style>
:root{
  --navy:#1c2433;
  --panel:rgba(22,26,34,.9);
  --accent:#29a3e0;
  --accent-dark:#1a78b8;
  --sky:#6cc6ec;
  --paper:#f7f7f7;
  --ink:#333;
  --white:#fff;
  --charcoal:#272727;
  --footer:#2b2b2b;
  --icon:#1e2a3a;
}
*{box-sizing:border-box;margin:0;padding:0}
html,body{width:1200px;height:3236px;overflow:hidden;background:var(--white)}
body{font-family:"Open Sans",Arial,sans-serif;color:var(--ink);position:relative}
section,header,footer{position:absolute;left:0;width:1200px}
.photo{background-color:#555}

/* Hero */
.hero{top:0;height:591px;overflow:hidden}
.hero-photo{position:absolute;inset:0;background:linear-gradient(100deg,#1b222e 0%,#232b39 40%,#3a4252 62%,#262d3a 80%,#4a3a34 100%)}
.brand{position:absolute;left:42px;top:38px;display:flex;align-items:center;gap:8px;color:var(--white);font-weight:600;font-size:19px;letter-spacing:.5px}
.brand-mark{width:14px;height:14px;background:var(--accent)}
.nav{position:absolute;left:700px;top:22px;display:flex;gap:21px}
.nav a{color:var(--white);text-decoration:none;font-size:12px;font-weight:600}
.hero-copy{position:absolute;left:54px;top:276px;width:512px;color:var(--white)}
.hero-copy h1{font-size:37px;font-weight:600;letter-spacing:-.5px;margin-bottom:6px}
.hero-copy p{font-style:italic;font-size:15px;line-height:19px}
.btn{display:inline-block;background:var(--accent);color:var(--white);font-size:13px;font-weight:600;text-decoration:none}
.hero-copy .btn{margin-top:24px;padding:10px 26px}
.estimate{position:absolute;left:745px;top:81px;width:367px;height:413px;background:var(--panel);padding:30px 33px;color:var(--white)}
.estimate h2{font-size:21px;font-weight:600;margin-bottom:22px}
.field{margin-bottom:12px}
.field label{display:block;font-size:8px;color:#aaa;text-transform:uppercase;margin-bottom:3px}
.select{height:34px;border:1px solid #777;font-size:10px;padding:0 8px;display:flex;align-items:center;justify-content:space-between}
.size-label{font-size:9px;font-weight:700;margin-top:18px}
.slider{position:relative;height:5px;background:var(--white);border-radius:3px;margin:14px 0 26px}
.slider span{position:absolute;left:190px;top:-10px;width:26px;height:26px;border-radius:50%;background:var(--accent);font-size:6px;display:flex;align-items:center;justify-content:center}
.total small{font-size:9px;font-weight:700}
.total strong{display:block;font-size:38px;font-weight:600}

/* Services */
.services{top:591px;height:562px;background:var(--paper)}
.section-title{text-align:center;font-size:26px;font-weight:400}
.services .section-title{padding-top:42px;color:#333}
.services hr{position:absolute;left:12px;width:1172px;top:83px;border:0;border-top:2px solid #d0d0d0}
.cards{position:absolute;top:92px;left:119px;display:flex;gap:24px}
.card{width:299px;height:450px;background:var(--white);box-shadow:0 1px 4px rgba(0,0,0,.2)}
.card-photo{height:268px}
.card h3{font-size:15px;font-weight:600;margin:26px 0 12px 25px}
.card ul{margin-left:42px;font-size:11.5px;line-height:22px;color:#444}
.card a{display:block;margin:10px 0 0 25px;font-size:10px;color:var(--accent);text-decoration:none;font-weight:600}

/* Roof types */
.roof-types{top:1153px;height:687px;background:#4b576a}
.roof-types .section-title{color:var(--white);padding-top:20px}
.type{position:absolute;width:302px;text-align:center;color:var(--white);font-size:15px;font-weight:600}
.type .swatch{height:204px;margin-bottom:14px;box-shadow:0 2px 8px rgba(0,0,0,.3)}
.coming{display:flex;align-items:center;justify-content:center;background:#3d4452;color:#8a8f98;font-size:30px;font-weight:400}

/* Projects */
.projects{top:1840px;height:565px}
.tile{position:absolute}
.latest{background:var(--charcoal);color:var(--white);padding:84px 0 0 34px}
.latest h2{font-size:29px;font-weight:400}
.latest .btn{margin:36px 0 0 108px;padding:8px 22px;font-size:19px;font-weight:400}
.feature{display:flex;flex-direction:column;align-items:center;padding-top:84px;color:var(--white)}
.feature h2{font-size:29px;font-weight:400}
.feature .more{margin-top:22px;padding:8px 30px;background:#d2d5da;color:var(--accent-dark);font-size:16px;font-weight:600}

/* Testimonial */
.testimonial{top:2405px;height:479px;background:linear-gradient(170deg,#34445e 0%,#4a4a52 35%,#8a4a30 65%,#2a1a14 100%);color:var(--white);text-align:center}
.testimonial h2{padding-top:80px;font-size:34px;font-weight:400}
.testimonial .sub{font-size:15px;margin-top:6px}
.quote{width:790px;margin:70px auto 0;font-size:15px;line-height:19px}
.reviewer{position:absolute;left:876px;top:354px;text-align:left;font-size:14px;line-height:18px}
.stars{position:absolute;left:204px;top:352px;color:#f5b400;font-size:13px;letter-spacing:12px}
.arrow{position:absolute;top:262px}
.dots{position:absolute;top:416px;left:566px;display:flex;gap:10px}
.dots i{width:7px;height:7px;border-radius:50%;background:rgba(255,255,255,.6)}
.dots i:first-child{background:var(--white)}

/* Contact */
.contact{top:2884px;height:276px;background:var(--sky);color:var(--white)}
.contact .section-title{padding-top:30px;font-size:29px}
.info{position:absolute;top:160px;display:flex;gap:14px}
.info h4{font-size:10px;font-weight:600}
.info p{font-size:9.5px;line-height:15px;margin-top:6px}

.site-footer{top:3160px;height:76px;background:var(--footer);color:#ccc;font-size:8px;text-align:center;line-height:76px}
</style>
</head>
<body>

<header class="hero">
  <div class="hero-photo" role="img" aria-label="Roofer in harness installing dark metal roof tiles"></div>
  <div class="brand"><span class="brand-mark"></span>STEADFAST ROOFING</div>
  <nav class="nav"><a href="#">HOME</a><a href="#">ABOUT US</a><a href="#">SERVICES</a><a href="#">PORTFOLIO</a><a href="#">CONTACT US</a></nav>
  <div class="hero-copy">
    <h1>BUILT RIGHT, BUILT TO LAST</h1>
    <p>After over a decade of general contracting, we continue to see a repetitive trend by the roof purchase process where homeowners are constantly left confused, nervous, and worried when they need a new roof. As one of the most important features of keeping your home safe, this is unacceptable. Steadfast Roofing was created to break this trend.</p>
    <a class="btn" href="#">REQUEST SERVICE</a>
  </div>
  <div class="estimate">
    <h2>INSTANT Estimate</h2>
    <div class="field"><label>Type of service</label><div class="select">Completely replace roof<span>⌄</span></div></div>
    <div class="field"><label>Location type</label><div class="select">Home/Residence<span>⌄</span></div></div>
    <div class="field"><label>Roofing material</label><div class="select">Tile<span>⌄</span></div></div>
    <div class="size-label">APROXIMATE ROOF SIZE (ft2)</div>
    <div class="slider"><span>1400</span></div>
    <div class="total"><small>TOTAL</small><strong>$6,110.00</strong></div>
  </div>
</header>

<section class="services">
  <h2 class="section-title">SERVICES</h2>
  <hr>
  <div class="cards">
    <article class="card">
      <div class="card-photo" role="img" aria-label="Hand inspecting metal roof tiles by a brick chimney" style="background:linear-gradient(180deg,#8a6456 0%,#6f7783 55%,#4d5663 100%)"></div>
      <h3>Roof Inspections</h3>
      <ul><li>Water stains on the ceiling</li><li>Damaged or broken panels</li><li>Missing or damaged shingles</li></ul>
      <a href="#">READ MORE &nbsp;&gt;</a>
    </article>
    <article class="card">
      <div class="card-photo" role="img" aria-label="Stacked metal roofing sheets being installed" style="background:linear-gradient(180deg,#9fb6cc 0%,#66707e 50%,#7d6a56 100%)"></div>
      <h3>Installation and Maintenance</h3>
      <ul><li>Shingles and metal roof installation</li><li>Rain gutters and downspouts cleaning</li><li>Ice dam formation prevention</li></ul>
      <a href="#">READ MORE &nbsp;&gt;</a>
    </article>
    <article class="card">
      <div class="card-photo" role="img" aria-label="Worker on wooden roof framing against the setting sun" style="background:linear-gradient(180deg,#7d8aa0 0%,#c79a62 55%,#6a5240 100%)"></div>
      <h3>Roof Replacement</h3>
      <ul><li>Ensure safety</li><li>Energy efficiency</li><li>Makes your home much easier to sell</li></ul>
      <a href="#">READ MORE &nbsp;&gt;</a>
    </article>
  </div>
</section>

<section class="roof-types">
  <h2 class="section-title">TYPES OF ROOFS</h2>
  <div class="type" style="left:112px;top:102px"><div class="swatch" role="img" aria-label="Cedar shake roof under blue sky" style="background:linear-gradient(180deg,#6aa2d8 0%,#a98a62 40%,#8e7150 100%)"></div>Cedar</div>
  <div class="type" style="left:442px;top:102px"><div class="swatch" role="img" aria-label="Standing seam metal roof on a house" style="background:linear-gradient(180deg,#d6dde3 0%,#6d7885 45%,#a9afb6 100%)"></div>Metal</div>
  <div class="type" style="left:770px;top:102px"><div class="swatch" role="img" aria-label="Slate tile roof" style="background:linear-gradient(180deg,#6e7683 0%,#81848f 100%)"></div>Slate</div>
  <div class="type" style="left:112px;top:380px"><div class="swatch" role="img" aria-label="Asphalt shingle roof over brick wall" style="background:linear-gradient(180deg,#cfd5db 0%,#5d616b 30%,#5d616b 65%,#a27c66 100%)"></div>Asphalt</div>
  <div class="type" style="left:442px;top:380px"><div class="swatch" role="img" aria-label="Flat rubber roof on a brick house" style="background:linear-gradient(180deg,#6f7f5a 0%,#2e3034 35%,#8a4e3e 100%)"></div>Rubber</div>
  <div class="type" style="left:770px;top:380px"><div class="swatch coming">COMING SOON</div></div>
</section>

<section class="projects">
  <div class="tile latest" style="left:0;top:0;width:384px;height:282px">
    <h2>Our latest projects</h2>
    <a class="btn" href="#">All projects</a>
  </div>
  <div class="tile feature" role="img" aria-label="Large house with grey roof in Lexington" style="left:384px;top:0;width:395px;height:282px;background:linear-gradient(180deg,#55595f,#45484c)">
    <h2>Lexington, MA</h2><span class="more">READ MORE</span>
  </div>
  <div class="tile" role="img" aria-label="Large grey shingled house with lawn" style="left:779px;top:0;width:421px;height:282px;background:linear-gradient(180deg,#5a8fd0 0%,#a9b3bd 55%,#6b9248 100%)"></div>
  <div class="tile" role="img" aria-label="Company truck parked at a white house under renovation" style="left:0;top:282px;width:384px;height:283px;background:linear-gradient(180deg,#9bb8d6 0%,#d9dde3 45%,#4a4c50 100%)"></div>
  <div class="tile" role="img" aria-label="Aerial view of house among trees" style="left:384px;top:282px;width:395px;height:283px;background:linear-gradient(180deg,#3d5a38 0%,#6e7b74 50%,#46663a 100%)"></div>
  <div class="tile" role="img" aria-label="Aerial view of white house with green lawn" style="left:779px;top:282px;width:421px;height:283px;background:linear-gradient(180deg,#3f5c38 0%,#c9cbc8 45%,#5d8c42 100%)"></div>
</section>

<section class="testimonial" role="img" aria-label="Clay tile roof under blue sky">
  <h2>Customer experience</h2>
  <p class="sub">Save Time and Money with a Top-Rated Service</p>
  <p class="quote">"We needed to put a new roof on our house, as well as repair a sagging porch roof. Shingles had been flying off and we had had several leaks. Dane provided a very reasonable estimate - well below some of the other HomeRater companies. The work was done very promptly and professionally. A couple of issues that arose were settled to our satisfaction and Dane took full ownership of the situation. It was very clear that customer satisfaction is a priority for this company. I would definitely recommend and hire again."</p>
  <div class="stars">★★★★★</div>
  <div class="reviewer">MARLA QUINT<br>Reviewer</div>
  <svg class="arrow" style="left:128px" width="20" height="30" viewBox="0 0 20 30"><path d="M15 3 4 15l11 12" fill="none" stroke="#fff" stroke-width="3"/></svg>
  <svg class="arrow" style="left:1052px" width="20" height="30" viewBox="0 0 20 30"><path d="M5 3l11 12L5 27" fill="none" stroke="#fff" stroke-width="3"/></svg>
  <div class="dots"><i></i><i></i><i></i><i></i></div>
</section>

<section class="contact">
  <h2 class="section-title">LET'S WORK TOGETHER</h2>
  <div class="info" style="left:120px">
    <svg width="36" height="36" viewBox="0 0 36 36"><circle cx="18" cy="18" r="14" fill="none" stroke="#1e2a3a" stroke-width="2.5"/><path d="M18 9v9l6 4" fill="none" stroke="#1e2a3a" stroke-width="2.5"/></svg>
    <div><h4>WORKING HOURS</h4><p>Mon - Sat 8.00 - 18.00<br>Sunday CLOSED</p></div>
  </div>
  <div class="info" style="left:386px">
    <svg width="30" height="36" viewBox="0 0 30 36"><path d="M15 33C6 22 4 17 4 13a11 11 0 0 1 22 0c0 4-2 9-11 20z" fill="none" stroke="#1e2a3a" stroke-width="2.5"/><circle cx="15" cy="13" r="4" fill="none" stroke="#1e2a3a" stroke-width="2.5"/></svg>
    <div><h4>LOCATION</h4><p>48 Alder Ln.<br>Brookfield MA 01500</p></div>
  </div>
  <div class="info" style="left:635px">
    <svg width="24" height="36" viewBox="0 0 24 36"><rect x="3" y="2" width="18" height="32" rx="3" fill="none" stroke="#1e2a3a" stroke-width="2.5"/><path d="M10 29h4" stroke="#1e2a3a" stroke-width="2"/></svg>
    <div><h4>CALL CENTAR</h4><p>555-014-2290</p></div>
  </div>
  <div class="info" style="left:868px">
    <svg width="36" height="30" viewBox="0 0 36 30"><path d="M2 14 33 2 26 28 16 19zM16 19l17-17M16 19v9l4-6" fill="none" stroke="#1e2a3a" stroke-width="2.2" stroke-linejoin="round"/></svg>
    <div><h4>WRITE US</h4><p>DaneMercer@SteadfastRoofingCo.com</p></div>
  </div>
</section>

<footer class="site-footer">Copyright © 2020 Steadfast Roofing. All Right Reserved</footer>

</body>
</html>
```